Business card for medical clinic

I need an upmarket, modern medical/health business card for my clinic

Contact Information for Business Card

name, address, email, qr code

```html
<!DOCTYPE html>
<html lang="en">
<head>
<meta charset="utf-8">
<title>Meridian Care Clinic – Business Card</title>
<link href="https://fonts.googleapis.com/css2?family=Montserrat:wght@500;700;800&family=Roboto:wght@400;500&display=swap" rel="stylesheet">
<style>
  :root{
    --backdrop:#2a2b2e;
    --navy:#1b2846;
    --navy-mid:#22345a;
    --sky:#2eaee4;
    --sky-soft:#3fb6e8;
    --steel:#3f7fa3;
    --white:#ffffff;
    --ink:#1e3a66;
  }
  *{box-sizing:border-box;margin:0;padding:0}
  html,body{width:1200px;height:960px;overflow:hidden}
  body{background:var(--backdrop);position:relative;font-family:"Roboto",sans-serif}

  .card{position:absolute;left:250px;width:700px;height:400px;border-radius:22px;overflow:hidden;box-shadow:0 14px 30px rgba(0,0,0,.45)}
  .card--front{top:60px;background:linear-gradient(45deg,var(--sky) 0%,var(--steel) 38%,var(--navy-mid) 68%,var(--navy) 100%)}
  .card--back{top:500px;background:var(--white)}

  /* brand lockup */
  .brand{position:absolute;display:flex;align-items:center;font-family:"Montserrat",sans-serif;font-weight:700;white-space:nowrap}
  .brand__dot{border-radius:50%;flex:none}
  .card--front .brand{left:0;right:0;top:150px;justify-content:center;gap:18px;color:var(--white);font-size:38px;letter-spacing:.06em}
  .card--front .brand__dot{width:40px;height:40px;border:4px solid var(--white)}
  .card--back .brand{left:30px;top:186px;gap:10px;color:var(--ink);font-size:17px;letter-spacing:.04em}
  .card--back .brand__dot{width:24px;height:24px;border:3px solid var(--ink)}

  .front-web{position:absolute;left:0;right:0;bottom:38px;display:flex;justify-content:center;align-items:center;gap:8px;color:var(--white);font-size:15px;letter-spacing:.03em}

  /* back panel */
  .panel-strip{position:absolute;left:345px;top:0;width:40px;height:400px;background:var(--navy-mid)}
  .panel-top{position:absolute;left:385px;top:0;right:0;height:120px;background:linear-gradient(120deg,var(--steel),var(--navy))}
  .panel-band{position:absolute;left:385px;top:120px;right:0;height:80px;background:var(--sky)}
  .panel-bottom{position:absolute;left:385px;top:290px;right:0;bottom:0;background:linear-gradient(120deg,var(--sky-soft),var(--navy))}
  .contact-tab{position:absolute;left:330px;top:150px;right:0;height:150px;background:var(--sky-soft);clip-path:polygon(0 0,100% 0,100% 100%,14% 100%,0 88%)}
  .tab-notch{position:absolute;left:332px;top:132px;width:0;height:0;border-left:20px solid transparent;border-bottom:18px solid var(--sky-soft)}

  .person{position:absolute;left:420px;top:40px;color:var(--white)}
  .person__name{font-family:"Montserrat",sans-serif;font-weight:800;font-size:24px;letter-spacing:.03em}
  .person__role{font-family:"Montserrat",sans-serif;font-weight:500;font-size:15px;letter-spacing:.04em;margin-top:2px}

  .icon-box{position:absolute;width:38px;height:34px;border-radius:4px;display:flex;align-items:center;justify-content:center}
  .icon-box--light{background:var(--sky)}
  .icon-box--dark{background:var(--navy-mid)}

  .info{position:absolute;color:var(--white);font-size:17px;line-height:1.35;letter-spacing:.02em}
  .info--phone{left:430px;top:160px}
  .info--mail{left:430px;top:230px}
  .info--address{left:430px;top:318px}
</style>
</head>
<body>

<section class="card card--front" aria-label="Card front">
  <div class="brand"><span class="brand__dot"></span>MERIDIAN CARE CLINIC</div>
  <div class="front-web">
    <svg width="16" height="16" viewBox="0 0 16 16" fill="none" stroke="#fff" stroke-width="1.3"><circle cx="8" cy="8" r="6.5"/><ellipse cx="8" cy="8" rx="3" ry="6.5"/><line x1="1.5" y1="8" x2="14.5" y2="8"/></svg>
    www.meridiancare.net
  </div>
</section>

<section class="card card--back" aria-label="Card back">
  <div class="brand"><span class="brand__dot"></span>MERIDIAN CARE CLINIC</div>

  <div class="panel-strip"></div>
  <div class="panel-top"></div>
  <div class="panel-band"></div>
  <div class="panel-bottom"></div>
  <div class="tab-notch"></div>
  <div class="contact-tab"></div>

  <div class="person">
    <div class="person__name">DANIEL REYES</div>
    <div class="person__role">MEDICAL DIRECTOR</div>
  </div>
  <div class="icon-box icon-box--light" style="left:640px;top:38px">
    <svg width="20" height="20" viewBox="0 0 20 20" fill="#fff"><circle cx="10" cy="6" r="4.5"/><path d="M2 19c0-5 3.5-7 8-7s8 2 8 7z"/></svg>
  </div>

  <div class="info info--phone">+0100 - 2468 - 13579<br>+0100 - 2468 - 13580</div>
  <div class="icon-box icon-box--dark" style="left:374px;top:166px">
    <svg width="18" height="18" viewBox="0 0 24 24" fill="#fff"><path d="M6.6 10.8a15 15 0 0 0 6.6 6.6l2.2-2.2a1 1 0 0 1 1-.25 11.4 11.4 0 0 0 3.6.57 1 1 0 0 1 1 1V20a1 1 0 0 1-1 1A17 17 0 0 1 3 4a1 1 0 0 1 1-1h3.5a1 1 0 0 1 1 1c0 1.25.2 2.45.57 3.57a1 1 0 0 1-.25 1z"/></svg>
  </div>

  <div class="info info--mail">hello@meridiancare.net<br>www.meridiancare.net</div>
  <div class="icon-box icon-box--dark" style="left:374px;top:236px">
    <svg width="20" height="18" viewBox="0 0 20 18" fill="none" stroke="#fff" stroke-width="2"><rect x="2" y="2" width="16" height="10" rx="1"/><line x1="10" y1="12" x2="10" y2="15"/><line x1="6" y1="16" x2="14" y2="16"/></svg>
  </div>

  <div class="info info--address">Harbor Lane 48,<br>Eastfield Park 210</div>
  <div class="icon-box icon-box--light" style="left:640px;top:316px">
    <svg width="20" height="18" viewBox="0 0 20 18" fill="#fff"><path d="M10 1 1 9h3v8h4.5v-5h3v5H16V9h3z"/></svg>
  </div>
</section>

</body>
</html>
```